Brochure Design Project - Innovative Service for Pharma Industry

Our start up is based in Germany, near Munich and we provide an innovative Service for the pharma industry. We develop product trainings and general trainings online. The adressed audience for these trainings are pharmacies and medics. The parma industry could increase the number of trainings, while saving money (incl a success guarantee). Our (not yet finnished) corporate page can be reviewed here: www.brevoloq.biz, our 'product & service' page is www.kestrumlearn.com. The color code should be leaned towards the corporate page.

The brochure should be send to decision makers in the pharma industry and rise the interest in innovative service. Seriousity should meet modern & clear design.Something eye cathing on the front page might be required.

Target Market(s)

Usually more conservative decision makers within the pharma industry

Industry/Entity Type

Industry

Requirements
Must have
• Conceptional design for an brochure (Din A4 size) of approx 6-8 pages, that capture the key messages (exact content would be filled / provided from us)
Nice to have
• Implementing some of the pics / phrases on the home page www.brevolq.biz could be maybe nice. How about a personal statement from the founder combined with a pic(pic attached)? Both is no must....

```html
<!DOCTYPE html>
<html lang="de">
<head>
<meta charset="utf-8">
<title>Brevoloq – Services</title>
<link href="https://fonts.googleapis.com/css2?family=Didact+Gothic&display=swap" rel="stylesheet">
<style>
  :root {
    --page-bg: #ffffff;
    --band-grey: #8d9292;
    --rule-grey: #9a9e9e;
    --accent: #e8491d;
    --body-text: #6a6a6a;
    --photo-light: #f1ede8;
    --photo-mid: #b9a393;
    --photo-dark: #4a2f26;
  }
  * { margin: 0; padding: 0; box-sizing: border-box; }
  html, body {
    width: 1200px;
    height: 908px;
    overflow: hidden;
    background: var(--page-bg);
  }
  .page {
    position: relative;
    width: 1200px;
    height: 908px;
    overflow: hidden;
    background: var(--page-bg);
    font-family: "Didact Gothic", "Century Gothic", sans-serif;
    color: var(--body-text);
  }
  .page-shape {
    position: absolute;
    left: 0;
    top: 0;
  }
  .section-title {
    position: absolute;
    left: 33px;
    top: 152px;
    font-size: 37px;
    font-weight: 400;
    color: var(--accent);
    letter-spacing: 0.2px;
  }
  .copy {
    position: absolute;
    left: 33px;
    font-size: 19.5px;
    line-height: 26px;
  }
  .copy-intro { top: 233px; }
  .copy-pitch { top: 361px; }
  .copy-audience { top: 515px; }
  .page-number {
    position: absolute;
    left: 33px;
    top: 858px;
    font-size: 20px;
  }
  .team-photo {
    position: absolute;
    left: 705px;
    top: 212px;
    width: 485px;
    height: 485px;
    background:
      radial-gradient(ellipse at 78% 60%, var(--photo-dark) 0%, rgba(74,47,38,0.6) 28%, rgba(74,47,38,0) 55%),
      radial-gradient(ellipse at 45% 55%, var(--photo-mid) 0%, rgba(185,163,147,0) 60%),
      linear-gradient(180deg, var(--photo-light) 0%, #e6ddd5 70%, #8c5a4f 100%);
  }
</style>
</head>
<body>
<main class="page">
  <svg class="page-shape" width="1200" height="908" viewBox="0 0 1200 908" aria-hidden="true">
    <rect x="0" y="0" width="677" height="908" fill="var(--band-grey)"/>
    <circle cx="77" cy="454" r="575" fill="var(--page-bg)"/>
    <rect x="0" y="0" width="430" height="2" fill="var(--rule-grey)"/>
  </svg>

  <h1 class="section-title">Services</h1>

  <p class="copy copy-intro">
    (Here should be a short description of what<br>
    your services and trainings are<br>
    and how are you different from the others.)<br>
    Example:
  </p>

  <p class="copy copy-pitch">
    Brevoloq entwickelt neuartige E-Learning Konzepte<br>
    und bietet diese als Plattform<br>
    für speziell definierte Zielmärkte und deren<br>
    gesamte Industrie an.
  </p>

  <p class="copy copy-audience">
    Wenn Ihr Unternehmen in der Pharmazeutischen<br>
    Entwicklung tätig ist, gehören&nbsp; Sie zu unseren<br>
    Top-Zielkunden.<br>
    Unsere CLOUD basierenden E-Learning Lösungen<br>
    erlauben es Ihnen sich auf das Wesentliche zu<br>
    konzentrieren: auf die Entwicklung neuer Produkte.<br>
    Wir übernehmen das Produkttraining.
  </p>

  <div class="team-photo" role="img" aria-label="Photo of three business people seated at a meeting table, a smiling woman in a dark suit in front taking notes"></div>

  <span class="page-number">5</span>
</main>
</body>
</html>
```